Buch-/eBook-Cover zum Thema Geldmanagement
Zielgruppe
ich benötige ein Buch-Cover (Vorder- und Rückseite) für das Buch Der Pfad der klaren Vermögensführung. Untertitel ist Innere Ruhe und Wohlstand vereint. Das genaue Format ist im Briefing hinterlegt
Aufgabenstellung
Schön wäre es, wenn das Cover hell gehalten wäre. Es soll hochwertig aussehen. Ich habe zwar eigenes Bild-Material angegeben, es können jedoch auch andere Vorschläge kommen.

```html
<!DOCTYPE html>
<html lang="de">
<head>
<meta charset="utf-8">
<title>Der Pfad der klaren Vermögensführung – Cover</title>
<link href="https://fonts.googleapis.com/css2?family=Oswald:wght@600&family=Josefin+Sans:wght@400&family=Open+Sans:wght@400;700&display=swap" rel="stylesheet">
<style>
  :root {
    --page-bg: #e9e9e7;
    --cover-light: #f7f7f6;
    --cover-mid: #e4e5e6;
    --gold: #c9a232;
    --ink: #1c1c1c;
    --panel: #ffffff;
    --sand-shadow: #d3d4d6;
  }
  * { margin: 0; padding: 0; box-sizing: border-box; }
  html, body { width: 1200px; height: 800px; overflow: hidden; }
  body {
    background: var(--page-bg);
    display: flex;
    justify-content: center;
    align-items: center;
    gap: 40px;
  }
  .cover {
    position: relative;
    width: 500px;
    height: 730px;
    background: linear-gradient(180deg, var(--cover-light) 0%, var(--cover-mid) 45%, var(--cover-light) 100%);
    box-shadow: 0 6px 22px rgba(0,0,0,0.18);
    overflow: hidden;
  }

  /* Back cover */
  .back-panel {
    position: absolute;
    left: 100px;
    right: 0;
    top: 80px;
    background: var(--panel);
    padding: 36px 28px 30px 38px;
  }
  .back-title {
    font-family: "Open Sans", sans-serif;
    font-weight: 700;
    font-size: 21px;
    line-height: 1.1;
    text-align: center;
    color: var(--ink);
    text-transform: uppercase;
    letter-spacing: 0.5px;
  }
  .back-blurb {
    margin-top: 32px;
    font-family: "Open Sans", sans-serif;
    font-size: 14px;
    line-height: 1.5;
    color: var(--ink);
    text-align: justify;
  }
  .back-author {
    margin-top: 36px;
    font-family: "Josefin Sans", sans-serif;
    font-size: 18px;
    letter-spacing: 3px;
    color: var(--ink);
  }
  .back-image {
    position: absolute;
    left: 160px;
    top: 570px;
    width: 240px;
    height: 145px;
    border-radius: 50% / 40%;
    background: radial-gradient(ellipse at 50% 30%, rgba(217,138,28,0.55) 0%, rgba(255,255,255,0.9) 35%, var(--sand-shadow) 75%, rgba(231,231,232,0) 100%);
  }

  /* Front cover */
  .front-title {
    position: absolute;
    left: 0;
    right: 0;
    top: 80px;
    text-align: center;
  }
  .title-main {
    font-family: "Oswald", sans-serif;
    font-weight: 600;
    color: var(--gold);
    text-transform: uppercase;
    line-height: 1;
  }
  .title-main--top { font-size: 100px; letter-spacing: 3px; }
  .title-main--bottom { font-size: 50px; letter-spacing: 0; margin-top: 8px; }
  .title-middle {
    display: flex;
    align-items: center;
    justify-content: center;
    gap: 12px;
    margin-top: 14px;
    font-family: "Josefin Sans", sans-serif;
    font-size: 26px;
    letter-spacing: 6px;
    color: var(--ink);
    text-transform: uppercase;
  }
  .title-middle .rule { width: 36px; height: 2px; background: var(--ink); }
  .subtitle {
    margin-top: 16px;
    font-family: "Josefin Sans", sans-serif;
    font-size: 16px;
    letter-spacing: 2px;
    color: var(--ink);
    text-transform: uppercase;
  }
  .front-image {
    position: absolute;
    left: 40px;
    right: 40px;
    top: 420px;
    height: 250px;
    border-radius: 50% / 35%;
    background: radial-gradient(ellipse at 50% 30%, rgba(217,138,28,0.5) 0%, rgba(190,186,176,0.75) 30%, var(--sand-shadow) 60%, rgba(231,231,232,0) 100%);
  }
  .front-author {
    position: absolute;
    left: 0;
    right: 0;
    bottom: 28px;
    text-align: center;
    font-family: "Josefin Sans", sans-serif;
    font-size: 22px;
    letter-spacing: 5px;
    color: var(--ink);
  }
</style>
</head>
<body>
  <section class="cover cover--back">
    <div class="back-panel">
      <h2 class="back-title">Der Pfad der klaren<br>Vermögensführung</h2>
      <p class="back-blurb">Haben Sie sich schon immer gefragt, was es für ein bewusstes Geldmanagement braucht und wie es Ihnen gelingen kann, in den Zustand von Fülle zu kommen? Wussten Sie, dass es eine Verbindung zwischen Geld und Spiritualität gibt? Möchten Sie wissen, wie Sie in den Geldfluss kommen können und auf welche Art und Weise sich Ihr finanzielles Handeln langfristig zum Positiven verändert? Dann lesen Sie jetzt dieses Buch!</p>
      <p class="back-author">AUTOR NAME</p>
    </div>
    <div class="back-image" role="img" aria-label="Foto: Schmetterling auf gestapelten weißen Steinen im Zen-Sand"></div>
  </section>

  <section class="cover cover--front">
    <header class="front-title">
      <h1 class="title-main title-main--top">Der Pfad</h1>
      <div class="title-middle"><span class="rule"></span><span>der klaren</span><span class="rule"></span></div>
      <div class="title-main title-main--bottom">Vermögensführung</div>
      <p class="subtitle">- Innere Ruhe und Wohlstand vereint -</p>
    </header>
    <div class="front-image" role="img" aria-label="Foto: Schmetterling auf einem Münzstapel im geharkten Zen-Sand"></div>
    <p class="front-author">AUTOR NAME</p>
  </section>
</body>
</html>
```